Flyer-Design für regional agierendes Immobilienbüro
Zielgruppe
*regional agierendes Immobilienbüro
*Vermittlung von privaten Wohnimmobilien (Einfamilienhäuser, Wohnungen, Grundstücke)
*projektbezogene Zielgruppe: Immobilien Eigentümer / Verkäufer /Vermieter
*Idee: Gutschein über eine von drei Serviceleistungen - kostenlos*:
- Wertermittlung vom geprüften Preisbild-Berater
- Wohnflächen-Check
- Unterlagen-Check
*für Verkäufer / Vermieter im Wert von EUR 349,-
Aufgabenstellung
*CI (Style Guide, diverse Grafiken und Logos in verschiedenen Formaten vorhanden)
*cleanes, modernes Design - dennoch Eyecatcher (Postwurf)
*Ggf. DIN lang
Der Schlüssel zu einem erfolgreichen Verkauf liegt in der sorgfältigen Vorbereitung!
Passt der Verkaufspreis?
Sind alle Unterlagen vollständig und vorab auf mögliche 'Stolpersteine' geprüft?
Stimmt die Wohnfläche und sind alle Angaben rechtssicher korrekt?
Gerne prüfen wir, ob die grundlegenden Voraussetzungen für einen reibungslosen Verkauf Ihrer Immobilie zum bestmöglichen Verkaufspreis passen - kostenlos und unverbindlich! Im Rahmen eines unverbindlichen Beratungsgesprächs erfahren Sie auch, wie Sie von unserem vollumfänglichen Vermarktungsservice profitieren können.
Rufen Sie am besten gleich an und vereinbaren Sie einen Termin mit uns!

```html
<!DOCTYPE html>
<html lang="de">
<head>
<meta charset="utf-8">
<title>Gutschein-Flyer LINDHOFER Immobilien</title>
<link rel="stylesheet" href="https://fonts.googleapis.com/css2?family=Fira+Sans+Extra+Condensed:ital,wght@0,400;0,500;1,300;1,400;1,600;1,700&display=swap">
<style>
  :root {
    --page: #ffffff;
    --petrol-dark: #0b4660;
    --petrol-light: #33718d;
    --ink: #0a0a0c;
    --gold: #c9a068;
    --gold-dark: #9c7a4c;
    --gold-light: #d8b27c;
    --white: #ffffff;
    --photo-dark: #1f2a30;
    --photo-light: #8c9498;
  }
  * { box-sizing: border-box; margin: 0; padding: 0; }
  html, body {
    width: 849px; height: 1200px; overflow: hidden;
    background: var(--page);
    font-family: "Fira Sans Extra Condensed", "Arial Narrow", sans-serif;
  }
  .flyer {
    position: absolute; left: 222px; top: 176px;
    width: 404px; height: 849px;
    box-shadow: 2px 3px 6px rgba(0,0,0,0.25);
    background: var(--white);
    color: var(--white);
  }
  .questions {
    position: absolute; left: 0; top: 0; width: 404px; height: 283px;
    background: linear-gradient(180deg, var(--petrol-dark) 0%, var(--petrol-light) 100%);
    padding: 20px 14px 0 20px;
    font-style: italic; font-size: 15px; line-height: 20px;
  }
  .questions p { margin-bottom: 21px; }
  .questions .intro { font-weight: 300; }
  .questions .question { font-weight: 600; letter-spacing: -0.1px; }
  .questions .offer { font-weight: 300; font-size: 14.5px; letter-spacing: -0.35px; }
  .questions .cta { font-weight: 600; }
  .photo {
    position: absolute; left: 0; top: 285px; width: 404px; height: 320px;
    background: radial-gradient(ellipse at 50% 40%, var(--photo-light) 0%, #4a5358 40%, var(--photo-dark) 80%);
  }
  .cut-line {
    position: absolute; left: 0; width: 404px; height: 14px;
  }
  .cut-line.upper { top: 598px; }
  .cut-line.lower { top: 780px; }
  .voucher-band {
    position: absolute; left: 0; top: 605px; width: 404px; height: 96px;
    background: var(--ink);
  }
  .voucher-title {
    position: absolute; left: 21px; top: 30px;
    font-size: 30px; line-height: 36px; font-weight: 700; font-style: italic;
    color: var(--gold); letter-spacing: -0.3px; white-space: nowrap;
  }
  .voucher-services {
    position: absolute; left: 238px; top: 18px; list-style: none;
    font-size: 16.5px; line-height: 22px; font-weight: 700; font-style: italic;
    color: var(--gold); white-space: nowrap;
  }
  .value-band {
    position: absolute; left: 0; top: 701px; width: 404px; height: 86px;
    background: linear-gradient(90deg, var(--gold-light) 0%, var(--gold) 60%, var(--gold-dark) 100%);
    padding: 14px 10px 0 20px;
    font-style: italic;
  }
  .value-band .value { font-size: 15px; line-height: 20px; font-weight: 600; }
  .value-band .terms { font-size: 11.5px; line-height: 16px; font-weight: 300; }
  .contact-band {
    position: absolute; left: 0; top: 787px; width: 404px; height: 62px;
    background: linear-gradient(180deg, var(--petrol-dark) 0%, var(--petrol-light) 100%);
    text-align: center; padding-top: 14px;
    font-size: 12.5px; line-height: 17px; font-weight: 400;
  }
  .contact-band .phone { font-weight: 500; }
  .contact-band .sep { margin: 0 3px; }
</style>
</head>
<body>
  <article class="flyer">
    <section class="questions">
      <p class="intro">Können Sie diese 3 Fragen mit JA beantworten?</p>
      <p class="question">- Passt der von Ihnen ermittelte Verkaufspreis?</p>
      <p class="question">- Stimmt die Wohnfläche und sind alle Angaben rechtssicher?</p>
      <p class="question">- Sind alle Unterlagen vollständig und auf Stolpersteine geprüft?</p>
      <p class="offer">Wir bieten mit unserem Gutschein Hilfestellung bei der Beantwortung<br>dieser Fragen. Für Sie vollkommen unverbindlich und kostenlos!</p>
      <p class="cta">Jetzt Gutschein einlösen und Sicherheit schaffen!</p>
    </section>

    <div class="photo" role="img" aria-label="Foto: Hände mit Kugelschreiber prüfen Lage- und Denkmalschutzpläne auf einem Schreibtisch"></div>

    <section class="voucher-band">
      <div class="voucher-title">GUTSCHEIN ÜBER:</div>
      <ul class="voucher-services">
        <li>- WERTERMITTLUNG</li>
        <li>- WOHNFLÄCHEN-CHECK</li>
        <li>- UNTERLAGEN-CHECK</li>
      </ul>
    </section>

    <svg class="cut-line upper" viewBox="0 0 404 14" aria-hidden="true">
      <line x1="0" y1="7" x2="372" y2="7" stroke="#ffffff" stroke-width="1.3" stroke-dasharray="3 2"/>
      <g fill="none" stroke="#ffffff" stroke-width="1.5">
        <circle cx="396" cy="3.5" r="2.6"/>
        <circle cx="396" cy="10.5" r="2.6"/>
        <line x1="393.8" y1="5" x2="377" y2="10"/>
        <line x1="393.8" y1="9" x2="377" y2="4"/>
      </g>
    </svg>

    <section class="value-band">
      <p class="value">Mit diesem Gutschein erhalten Verkäufer / Vermieter eine der 3 oben genannten Serviceleistungen im Wert von 349 € kostenlos!</p>
      <p class="terms">Gültig bis 31.12.2018, keine Barauszahlung möglich.</p>
    </section>

    <section class="contact-band">
      <p>LINDHOFER Immobilien<span class="sep">|</span>Jonas Beispiel<span class="sep">|</span>Lindenweg 12<span class="sep">|</span>12345 Beispielstadt</p>
      <p><span class="phone">Telefon: 01234 98 76 540</span><span class="sep">|</span>www.lindhofer-immo.de</p>
    </section>

    <svg class="cut-line lower" viewBox="0 0 404 14" aria-hidden="true">
      <line x1="32" y1="7" x2="404" y2="7" stroke="#ffffff" stroke-width="1.3" stroke-dasharray="3 2"/>
      <g fill="none" stroke="#ffffff" stroke-width="1.5">
        <circle cx="8" cy="3.5" r="2.6"/>
        <circle cx="8" cy="10.5" r="2.6"/>
        <line x1="10.2" y1="5" x2="27" y2="10"/>
        <line x1="10.2" y1="9" x2="27" y2="4"/>
      </g>
    </svg>
  </article>
</body>
</html>
```